wedding invitation card

Requirement:
1. White background, pink elements on the card, simple elegant looking
2. content:
Please join us as we celebrate new beginnings, new dreams,
and most importantly, new love at the marriage of
Miss Lin Qiao and Mr. Haoran Bei
Friday, The First of January
Two Thousand Fifteen at Eleven o’clock
Coral Breeze Hotel Palm Garden Deck.

Reception will be followed at Lantern Hall at Half-Past Twelve o'clock

Please RSVP before December 18th 2015 by email: qiaolin0317@mailnest.example

3. Flat paper
4. be able to change the size of the design according to printing requirement

```html
<!DOCTYPE html>
<html lang="en">
<head>
<meta charset="utf-8">
<title>Wedding Invitation – Lin Qiao &amp; Haoran Bei</title>
<link rel="stylesheet" href="https://fonts.googleapis.com/css2?family=Pinyon+Script&family=Nunito+Sans:wght@300;400&family=Cormorant+Garamond:ital,wght@1,400;1,700&display=swap">
<style>
  :root {
    --board: #d8d8d8;
    --paper: #ffffff;
    --edge: #c4c4c4;
    --plum: #a8489a;
    --plum-deep: #8e1f6a;
    --ink: #555555;
    --rule: #8a8a8a;
    --label: #f4f4f4;
    --petal-violet: #9b7cc4;
    --petal-blue: #3fb3dd;
    --petal-pink: #eab2cf;
  }
  * { margin: 0; padding: 0; box-sizing: border-box; }
  html, body {
    width: 1200px; height: 759px; overflow: hidden;
    background: var(--board);
  }
  .board { position: relative; width: 1200px; height: 759px; }

  .card {
    position: absolute;
    background: var(--paper);
    border: 1px solid var(--edge);
    overflow: hidden;
  }
  .card--front { left: 96px; top: 126px; width: 494px; height: 247px; }
  .card--back  { left: 102px; top: 417px; width: 494px; height: 248px; }
  .card--open  { left: 629px; top: 95px; width: 493px; height: 495px; }

  .floral { position: absolute; display: block; }

  .view-label {
    position: absolute;
    font-family: "Cormorant Garamond", serif;
    font-style: italic;
    font-size: 15px;
    color: var(--label);
  }

  .title-script {
    position: absolute; left: 264px; top: 138px;
    font-family: "Pinyon Script", cursive;
    font-size: 44px; color: var(--plum);
    line-height: 1;
  }

  .date-mark {
    position: absolute; left: 56px; top: 174px;
    font-family: "Cormorant Garamond", serif;
    font-style: italic; font-weight: 700;
    font-size: 11px; color: var(--plum-deep);
  }

  .fold-line {
    position: absolute; left: 0; top: 246px; width: 100%; height: 1px;
    background: linear-gradient(to right, #eeeeee, #e2e2e2, #eeeeee);
  }

  .invite-lead {
    position: absolute; left: 0; top: 272px; width: 100%;
    text-align: center;
    font-family: "Nunito Sans", sans-serif; font-weight: 300;
    font-size: 12.5px; line-height: 15.5px; color: var(--plum);
  }

  .couple {
    position: absolute; left: 0; top: 316px; width: 100%;
    font-family: "Pinyon Script", cursive; color: var(--plum);
    line-height: 1;
  }
  .couple__bride { position: absolute; left: 133px; top: 0; font-size: 38px; white-space: nowrap; }
  .couple__and   { position: absolute; left: 246px; top: 34px; font-size: 22px; }
  .couple__groom { position: absolute; left: 128px; top: 44px; font-size: 38px; white-space: nowrap; }
  .couple small { font-size: 24px; }

  .details {
    position: absolute; left: 0; top: 437px; width: 100%;
    font-family: "Nunito Sans", sans-serif; font-weight: 400;
    font-size: 7.2px; line-height: 9.2px; color: var(--ink);
  }
  .details__col { position: absolute; top: 0; }
  .details__col--when  { left: 41px; }
  .details__col--where { left: 158px; }
  .details__col--rsvp  { left: 337px; }
  .details__rule {
    position: absolute; top: -3px; width: 1px; height: 52px;
    background: var(--rule);
  }
  .details__rule--one { left: 141px; }
  .details__rule--two { left: 327px; }
</style>
</head>
<body>
<main class="board">

  <section class="card card--front" aria-label="Card front">
    <svg class="floral" width="494" height="247" viewBox="0 0 494 247" role="img" aria-label="Watercolour wreath of violet, blue and pink butterfly blossoms">
      <defs>
        <linearGradient id="wreath-front" x1="0" y1="0" x2="1" y2="0">
          <stop offset="0" stop-color="var(--petal-violet)" stop-opacity="0.55"/>
          <stop offset="0.45" stop-color="var(--petal-blue)" stop-opacity="0.5"/>
          <stop offset="1" stop-color="var(--petal-pink)" stop-opacity="0.55"/>
        </linearGradient>
      </defs>
      <path d="M0 0 L50 0 Q40 80 70 110 Q140 150 230 120 Q300 90 310 0 L330 0 Q335 100 300 150 Q240 200 150 185 Q60 200 0 185 Z" fill="url(#wreath-front)"/>
    </svg>
    <div class="title-script">Invitation</div>
  </section>
  <div class="view-label" style="left:106px; top:378px;">front (200 x 100 mm)</div>

  <section class="card card--back" aria-label="Card back">
    <svg class="floral" width="494" height="248" viewBox="0 0 494 248" role="img" aria-label="Watercolour sweep of violet, blue and pink butterfly blossoms">
      <defs>
        <linearGradient id="wreath-back" x1="0" y1="0" x2="1" y2="0">
          <stop offset="0" stop-color="var(--petal-violet)" stop-opacity="0.5"/>
          <stop offset="0.55" stop-color="var(--petal-blue)" stop-opacity="0.45"/>
          <stop offset="1" stop-color="var(--petal-violet)" stop-opacity="0.55"/>
        </linearGradient>
      </defs>
      <path d="M200 0 L280 0 Q270 60 330 90 Q400 110 440 60 Q470 30 470 0 L494 0 L494 130 Q450 175 390 175 Q300 180 260 140 Q210 90 200 0 Z" fill="url(#wreath-back)"/>
    </svg>
    <div class="date-mark">1.01.2016</div>
  </section>
  <div class="view-label" style="left:128px; top:671px;">back</div>

  <section class="card card--open" aria-label="Card opened">
    <svg class="floral" style="left:205px; top:92px;" width="105" height="78" viewBox="0 0 105 78" role="img" aria-label="Small cluster of watercolour butterfly blossoms">
      <defs>
        <radialGradient id="cluster" cx="0.5" cy="0.45" r="0.55">
          <stop offset="0" stop-color="var(--petal-violet)" stop-opacity="0.6"/>
          <stop offset="0.7" stop-color="var(--petal-pink)" stop-opacity="0.45"/>
          <stop offset="1" stop-color="var(--petal-pink)" stop-opacity="0"/>
        </radialGradient>
      </defs>
      <ellipse cx="55" cy="38" rx="50" ry="36" fill="url(#cluster)"/>
    </svg>
    <div class="fold-line"></div>

    <p class="invite-lead">Please join us as we celebrate new beginnings, new dreams,<br>and most importantly, new love at the marriage of</p>

    <div class="couple">
      <div class="couple__bride"><small>miss</small> Lin Qiao</div>
      <div class="couple__and">and</div>
      <div class="couple__groom"><small>mr.</small> Haoran Bei</div>
    </div>

    <div class="details">
      <div class="details__col details__col--when">FRIDAY,<br>THE FIRST OF JANUARY<br>Two Thousand Fifteen<br>at Eleven o'clock</div>
      <span class="details__rule details__rule--one"></span>
      <div class="details__col details__col--where">Coral Breeze Hotel Palm Garden Deck.<br><br>Reception will be followed<br>at Lantern Hall at Half-Past Twelve o'clock</div>
      <span class="details__rule details__rule--two"></span>
      <div class="details__col details__col--rsvp">Please RSVP<br>before December 18th 2015<br>by email: qiaolin0317@mailnest.example</div>
    </div>
  </section>
  <div class="view-label" style="left:632px; top:614px;">open (200 x 200 mm)</div>

</main>
</body>
</html>
```